Classy, Elegant, Simple Business Card Design

Looking to have a classy, simple, and elegant design. Want a top notch designed business card. I really like the look of the new brivo credit card. I also like the design I attached. I am trying to reach 21-29 year old females for booking us for there wedding or event. We offer Disc Jockey Service, Photo Booth Rentals, and Uplighting .

Target Market(s)

21-28 year old females

Contact Information for Business Card

Has to have logo, website, email, and phone number

Font styles to use
Other font styles liked:
• open to font choice, modern, clean
Designer to choose
33a6d7
0791cd
0555a3
ffffff

Requirements
Must have
• Has to have logo, website, email, and phone number
Nice to have
• I really like the design of the new brivo credit card. I also included my logo and some designs I like
Should not have
• clutter or too much info

```html
<!DOCTYPE html>
<html lang="en">
<head>
<meta charset="utf-8">
<title>Tidewell Event Group – Business Card</title>
<link rel="stylesheet" href="https://fonts.googleapis.com/css2?family=Raleway:wght@500;600&display=swap">
<style>
  :root {
    --bg: #e9e9e9;
    --card: #f7f7f7;
    --card-edge: #dcdcdc;
    --brand: #0791cd;
    --ink: #3d65b5;
  }
  * { margin: 0; padding: 0; box-sizing: border-box; }
  html, body {
    width: 1200px; height: 1200px; overflow: hidden;
    background: var(--bg);
    font-family: "Raleway", sans-serif;
  }
  .card {
    position: absolute;
    left: 251px;
    width: 697px;
    height: 398px;
    background: var(--card);
    border: 1px solid var(--card-edge);
  }
  .card--front { top: 115px; }
  .card--back  { top: 660px; }

  .brand-name {
    position: absolute;
    color: var(--brand);
    font-weight: 600;
    white-space: nowrap;
    display: flex;
    align-items: center;
  }
  .brand-name .dot {
    display: inline-block;
    border-radius: 50%;
    background: var(--brand);
  }
  .card--front .brand-name {
    left: 50%; top: 185px;
    transform: translateX(-50%);
    font-size: 30px;
    letter-spacing: 2px;
    gap: 12px;
  }
  .card--front .brand-name .dot { width: 14px; height: 14px; }

  .website {
    position: absolute;
    left: 0; right: 0; top: 351px;
    text-align: center;
    color: var(--ink);
    font-weight: 600;
    font-size: 17px;
    letter-spacing: 4px;
  }

  .card--back .brand-name {
    right: 38px; top: 46px;
    font-size: 14px;
    letter-spacing: 1px;
    gap: 6px;
  }
  .card--back .brand-name .dot { width: 8px; height: 8px; }

  .divider {
    position: absolute;
    left: 347px; top: 69px;
    width: 4px; height: 258px;
    background: var(--ink);
  }
  .contact {
    position: absolute;
    top: 185px;
    display: flex;
    align-items: center;
    color: var(--ink);
    font-weight: 500;
    font-size: 17px;
    letter-spacing: 3.5px;
    white-space: nowrap;
  }
  .contact svg { fill: var(--ink); display: block; }
  .contact--phone { left: 161px; gap: 22px; }
  .contact--email { left: 384px; gap: 20px; }
</style>
</head>
<body>
  <section class="card card--front">
    <div class="brand-name"><span class="dot"></span>Tidewell Event Group</div>
    <p class="website">www.yourwebsite.com</p>
  </section>

  <section class="card card--back">
    <div class="brand-name"><span class="dot"></span>Tidewell</div>
    <div class="divider"></div>
    <div class="contact contact--phone">
      <svg width="23" height="23" viewBox="0 0 24 24" aria-hidden="true">
        <path d="M6.6 10.8c1.4 2.8 3.8 5.1 6.6 6.6l2.2-2.2c.3-.3.7-.4 1-.2 1.1.4 2.3.6 3.6.6.6 0 1 .4 1 1V20c0 .6-.4 1-1 1C10.6 21 3 13.4 3 4c0-.6.4-1 1-1h3.5c.6 0 1 .4 1 1 0 1.3.2 2.5.6 3.6.1.3 0 .7-.2 1L6.6 10.8z"/>
      </svg>
      <span>+999 9999</span>
    </div>
    <div class="contact contact--email">
      <svg width="28" height="19" viewBox="0 0 28 19" aria-hidden="true">
        <path d="M0 0h28v1.5L14 11 0 1.5z"/>
        <path d="M0 4l14 9.5L28 4v15H0z"/>
      </svg>
      <span>your@e-mail.com</span>
    </div>
  </section>
</body>
</html>
```